Corvanta512 Business Card Redesign

I want to create a design for brand new business cards, I need something exceptional for clear plastic business card design. Please do not submit without it being on a clear design. Photos of the various logo versions attached.

```html
<!DOCTYPE html>
<html lang="en">
<head>
<meta charset="utf-8">
<title>Corvanta512 Clear Business Card</title>
<link rel="stylesheet" href="https://fonts.googleapis.com/css2?family=Work+Sans:wght@400;500;700&display=swap">
<style>
  :root {
    --backdrop: #c9c9c9;
    --plastic: rgba(255, 255, 255, 0.42);
    --plastic-edge: rgba(255, 255, 255, 0.85);
    --sheen: rgba(255, 255, 255, 0.55);
    --navy: #2e4674;
    --gold: #e1c17d;
    --gold-deep: #c9a24e;
    --ink: #1f2a44;
  }
  * { margin: 0; padding: 0; box-sizing: border-box; }
  html, body { width: 1200px; height: 1200px; overflow: hidden; }
  body {
    background: var(--backdrop);
    font-family: "Work Sans", Arial, sans-serif;
    position: relative;
  }
  .card {
    position: absolute;
    left: 150px;
    width: 900px;
    height: 514px;
    overflow: hidden;
    border-radius: 6px;
    background:
      linear-gradient(125deg, var(--sheen) 0%, rgba(255,255,255,0) 38%, rgba(255,255,255,0) 62%, rgba(255,255,255,0.35) 100%),
      var(--plastic);
    border: 1.5px solid var(--plastic-edge);
    box-shadow: 8px 10px 18px rgba(0,0,0,0.18), inset 0 0 0 1px rgba(255,255,255,0.4);
  }
  .card--front { top: 65px; }
  .card--back { top: 621px; }
  .front-shapes { position: absolute; inset: 0; }
  .contact-block { position: absolute; left: 71px; top: 102px; color: var(--ink); }
  .person-name {
    font-size: 42px; font-weight: 700; color: var(--navy);
    letter-spacing: 0.3px; line-height: 46px;
  }
  .person-role { font-size: 23px; line-height: 30px; margin-top: 16px; }
  .contact-list { list-style: none; margin-top: 38px; }
  .contact-list li {
    display: flex; align-items: flex-start; gap: 16px;
    font-size: 25px; line-height: 36px;
  }
  .contact-list .address { margin-top: 22px; }
  .icon { width: 18px; height: 18px; flex: none; margin-top: 9px; fill: var(--navy); }
  .wordmark {
    position: absolute;
    display: flex; align-items: center; gap: 14px;
    color: var(--gold-deep);
    font-weight: 700;
    letter-spacing: 1px;
    white-space: nowrap;
    transform: translate(-50%, -50%);
  }
  .wordmark__dot { border-radius: 50%; background: var(--gold-deep); flex: none; }
  .wordmark--front { left: 700px; top: 268px; font-size: 40px; }
  .wordmark--front .wordmark__dot { width: 24px; height: 24px; }
  .wordmark--back { left: 50%; top: 50%; font-size: 64px; }
  .wordmark--back .wordmark__dot { width: 36px; height: 36px; }
</style>
</head>
<body>
  <section class="card card--front">
    <svg class="front-shapes" width="900" height="514" viewBox="0 0 900 514">
      <ellipse cx="252" cy="262" rx="262" ry="330" fill="var(--navy)"/>
      <ellipse cx="266" cy="248" rx="248" ry="330" fill="var(--gold)"/>
    </svg>
    <div class="contact-block">
      <h1 class="person-name">DANA WHITLOCK</h1>
      <p class="person-role">Sales &amp; Estimating</p>
      <ul class="contact-list">
        <li><svg class="icon" viewBox="0 0 24 24"><path d="M6.6 10.8a15.1 15.1 0 0 0 6.6 6.6l2.2-2.2c.3-.3.7-.4 1-.2 1.1.4 2.3.6 3.6.6.6 0 1 .4 1 1V20c0 .6-.4 1-1 1A17 17 0 0 1 3 4c0-.6.4-1 1-1h3.5c.6 0 1 .4 1 1 0 1.3.2 2.5.6 3.6.1.3 0 .7-.2 1z"/></svg>(555) 014-2290</li>
        <li><svg class="icon" viewBox="0 0 24 24"><path d="M6 2h12v5H6zM4 8h16a2 2 0 0 1 2 2v7h-4v5H6v-5H2v-7a2 2 0 0 1 2-2zm4 8v4h8v-4z"/></svg>(555) 014-2291</li>
        <li><svg class="icon" viewBox="0 0 24 24"><path d="M2 5h20v14H2zm2 2v.5l8 5 8-5V7l-8 5z"/></svg>www.corvanta512.com</li>
        <li class="address"><svg class="icon" viewBox="0 0 24 24"><path d="M12 2a7 7 0 0 0-7 7c0 5.2 7 13 7 13s7-7.8 7-13a7 7 0 0 0-7-7zm0 9.5A2.5 2.5 0 1 1 12 6.5a2.5 2.5 0 0 1 0 5z"/></svg><span>48 Halden Ave Suite 210,<br>Brookfield, PA 19021</span></li>
      </ul>
    </div>
    <div class="wordmark wordmark--front"><span class="wordmark__dot"></span>Corvanta512</div>
  </section>

  <section class="card card--back">
    <div class="wordmark wordmark--back"><span class="wordmark__dot"></span>Corvanta512</div>
  </section>
</body>
</html>
```